sign business needs card design

I need a very clean design for my business card.
It is a sign company. Banners By Noon is the name of the business.
Our colors are orange, yellow. But I want a very professional card.
But you can use any colors. I like a black background with orange letters or a white back with a clean look. No cartoon or kiddy looking print. The info. I need on the card is as follows.
Banners By Noon
318.555.0172 ph.
318.555.0199 fax.
email.bannersbynoon@mailvista.net
web.bannersbynooninc.com
4187 N. Maplecrest Lane Ste. 2b
Dale Hutchins

```html
<!DOCTYPE html>
<html lang="en">
<head>
<meta charset="utf-8">
<title>Banners By Noon – Business Card</title>
<link rel="stylesheet" href="https://fonts.googleapis.com/css2?family=PT+Sans&family=PT+Sans+Narrow&display=swap">
<style>
  :root {
    --orange: #ef6428;
    --ghost: #fdeee6;
    --slate: #6d6e71;
    --icon: #8a8c8f;
    --paper: #ffffff;
    --stripe-start: #fff03a;
    --stripe-mid: #fbb21f;
    --stripe-end: #e63b2e;
  }
  html, body {
    margin: 0;
    padding: 0;
    overflow: hidden;
    background: var(--paper);
  }
  .card {
    position: relative;
    width: 1200px;
    height: 667px;
    background: var(--paper);
    overflow: hidden;
    font-family: "PT Sans", "Helvetica Neue", Arial, sans-serif;
  }
  .brand-ghost {
    position: absolute;
    left: 38px;
    top: 238px;
    margin: 0;
    font-size: 126px;
    line-height: 1;
    letter-spacing: 26px;
    color: var(--ghost);
    white-space: nowrap;
  }
  .brand-name {
    position: absolute;
    left: 50px;
    top: 150px;
    margin: 0;
    font-family: "PT Sans Narrow", "Arial Narrow", sans-serif;
    font-weight: 400;
    font-size: 80px;
    line-height: 1;
    color: var(--orange);
    white-space: nowrap;
  }
  .contact {
    position: absolute;
    left: 624px;
    top: 118px;
    margin: 0;
    padding: 0;
    list-style: none;
    color: var(--orange);
    font-size: 28px;
    line-height: 39px;
  }
  .contact li {
    position: relative;
    padding-left: 53px;
    white-space: nowrap;
  }
  .contact .icon {
    position: absolute;
    left: 0;
    top: 6px;
    width: 30px;
    height: 30px;
  }
  .contact .address { margin-bottom: 14px; }
  .contact .fax { margin-bottom: 14px; }
  .contact .phone { margin-bottom: 6px; }
  .contact .email { margin-bottom: 10px; }
  .stripe {
    position: absolute;
    left: 0;
    top: 423px;
    width: 1200px;
    height: 22px;
    background: linear-gradient(90deg, var(--stripe-start) 0%, var(--stripe-mid) 30%, #f7962a 60%, var(--stripe-end) 100%);
  }
  .footer-band {
    position: absolute;
    left: 0;
    top: 445px;
    width: 1200px;
    height: 222px;
    background: var(--slate);
  }
  .footer-name {
    position: absolute;
    left: 0;
    right: 0;
    top: 470px;
    margin: 0;
    text-align: center;
    font-family: "PT Sans Narrow", "Arial Narrow", sans-serif;
    font-weight: 400;
    font-size: 142px;
    line-height: 1;
    color: var(--orange);
    white-space: nowrap;
  }
</style>
</head>
<body>
<main class="card">
  <p class="brand-ghost" aria-hidden="true">Banners</p>
  <h1 class="brand-name">Banners By Noon</h1>

  <ul class="contact">
    <li class="address">
      <svg class="icon" viewBox="0 0 30 30" aria-hidden="true">
        <path d="M15 2a8 8 0 0 0-8 8c0 6 8 18 8 18s8-12 8-18a8 8 0 0 0-8-8z" fill="var(--icon)"/>
        <circle cx="15" cy="10" r="2" fill="#d52b1e"/>
      </svg>
      4187 N. Maplecrest Lane Ste. 2b<br>Dale Hutchins
    </li>
    <li class="fax">
      <svg class="icon" viewBox="0 0 30 30" aria-hidden="true">
        <rect x="3" y="12" width="24" height="13" rx="2" fill="var(--icon)"/>
        <rect x="8" y="5" width="14" height="9" fill="#dfe3ec" stroke="var(--icon)"/>
        <rect x="6" y="15" width="9" height="3" fill="#c7d3ea"/>
        <rect x="18" y="15" width="6" height="7" fill="#c7d3ea"/>
      </svg>
      318.555.0199 fax.
    </li>
    <li class="phone">
      <svg class="icon" viewBox="0 0 30 30" aria-hidden="true">
        <path d="M3 11c0-4 24-4 24 0v3h-6v-3H9v3H3z" fill="var(--icon)"/>
        <path d="M7 15h16l3 11H4z" fill="var(--icon)"/>
        <rect x="11" y="18" width="8" height="5" fill="#ffffff"/>
      </svg>
      318.555.0172 ph.
    </li>
    <li class="email">
      <svg class="icon" viewBox="0 0 30 30" aria-hidden="true">
        <circle cx="15" cy="15" r="12" fill="none" stroke="var(--icon)" stroke-width="2"/>
        <circle cx="15" cy="15" r="4.5" fill="none" stroke="var(--icon)" stroke-width="2"/>
        <path d="M19.5 11v6c0 3 4 3 4-1" fill="none" stroke="var(--icon)" stroke-width="2"/>
      </svg>
      email.bannersbynoon@mailvista.net
    </li>
    <li class="web">
      <svg class="icon" viewBox="0 0 30 30" aria-hidden="true">
        <circle cx="15" cy="15" r="12" fill="none" stroke="var(--icon)" stroke-width="1.5" stroke-dasharray="2 1.5"/>
        <ellipse cx="15" cy="15" rx="5" ry="12" fill="none" stroke="var(--icon)" stroke-width="1.2"/>
        <line x1="3" y1="15" x2="27" y2="15" stroke="var(--icon)" stroke-width="1.2"/>
      </svg>
      web.bannersbynooninc.com
    </li>
  </ul>

  <div class="stripe" aria-hidden="true"></div>
  <div class="footer-band" aria-hidden="true"></div>
  <p class="footer-name">Banners By Noon</p>
</main>
</body>
</html>
```